Kelvar Systems Website

Website design for our company: Kelvar Systems.
The website should look fresh and IT focused. Please have a look at http://www.kelvarsystems.net.au/ for our current design. We want something fresh and new, professional looking, in WordPress so we can easily make changes.

Industry/Entity Type

It Company

```html
<!DOCTYPE html>
<html lang="en">
<head>
<meta charset="utf-8">
<title>Kelvar Systems</title>
<link rel="stylesheet" href="https://fonts.googleapis.com/css2?family=Russo+One&family=Michroma&family=Open+Sans:wght@400;600&family=Arimo:wght@400;700&display=swap">
<style>
:root{
  --green:#2e9a34;
  --green-text:#1f9a2a;
  --dark:#333238;
  --header:#2b2b2b;
  --topbar:#3a3a3a;
  --footer:#262626;
  --bottom:#4a4a4a;
  --blush:#e3d9d7;
  --muted:#9a9aa0;
  --ink:#222;
  --white:#fff;
  --amber:#f3b92c;
}
*{box-sizing:border-box;margin:0;padding:0}
html,body{width:681px;height:1200px;overflow:hidden;background:var(--white)}
.page{position:relative;width:681px;height:1200px;overflow:hidden;font-family:"Arimo",Arial,sans-serif;color:var(--ink)}
.abs{position:absolute}

.topbar{left:0;top:0;width:681px;height:30px;background:var(--topbar)}
.ip{right:200px;top:10px;font-size:8px;color:#ddd}
.ip b{font-weight:400;color:var(--amber)}
.search{left:498px;top:8px;width:95px;height:16px;background:#cfcfcf;border-radius:2px;font-size:8px;color:#444;padding:3px 8px}
.radio{top:11px;font-size:8px;color:#eee;display:flex;align-items:center;gap:3px}
.radio i{width:8px;height:8px;border-radius:50%;background:#fff;display:inline-block}
.radio i.on{background:#3a6fb0;box-shadow:inset 0 0 0 2px #fff}
.navbar{left:0;top:30px;width:681px;height:38px;background:var(--header)}
.nav{right:7px;top:46px;display:flex;gap:17px;font-family:"Michroma",sans-serif;font-size:7px;color:#eee;letter-spacing:.3px}
.logo-tab{left:0;top:0}
.logo-name{left:40px;top:14px;width:70px;text-align:center;font-weight:700;font-size:11px;color:var(--white);line-height:1.1}

.hero{left:0;top:68px;width:681px;height:332px;background:linear-gradient(100deg,#f3f3f3 0%,#e7e5e3 40%,#cfccc9 62%,#6d6c6e 78%,#2a2a2c 100%)}
.hero-title{left:18px;top:208px;font-family:"Russo One",sans-serif;font-weight:400;font-size:21px;color:#1d1d1d;letter-spacing:.2px}
.hero-sub{left:20px;top:242px;font-size:12.5px;color:#333}
.code-input{left:18px;top:280px;width:167px;height:25px;background:#3a3a3c;color:#eee;font-size:10px;padding:7px 8px;border-radius:2px}
.connect{left:192px;top:280px;width:96px;height:25px;background:var(--green);color:#fff;font-family:"Russo One",sans-serif;font-size:10.5px;text-align:center;line-height:25px;border-radius:2px}

.blush{left:0;top:400px;width:681px;height:236px;background:var(--blush)}
.services{left:18px;top:370px;width:643px;height:248px;background:var(--dark)}
.more{left:559px;top:341px;width:100px;height:29px;background:#222;color:#fff;font-size:10px;text-align:center;line-height:29px}
.svc{width:260px}
.svc-icon{position:absolute;left:0;top:0;width:66px;height:66px;border-radius:50%;background:#e8e8e8;display:flex;align-items:center;justify-content:center}
.svc h3{position:absolute;left:81px;top:5px;font-family:"Russo One",sans-serif;font-weight:400;font-size:12.5px;color:#d8d8d8;white-space:nowrap}
.svc p{position:absolute;left:81px;top:23px;width:192px;font-family:"Open Sans",sans-serif;font-size:9.3px;line-height:11.8px;color:var(--muted)}

.clients-title{left:0;top:674px;width:681px;text-align:center;font-size:23.5px;font-weight:400;color:#2a2a2a}
.avatar{width:69px;height:69px;border-radius:50%;background:radial-gradient(circle at 50% 45%,#e9d3bf 0%,#d8c6b4 45%,#f1ebe4 75%)}
.quote{width:188px;font-family:"Open Sans",sans-serif;font-size:10px;line-height:11.6px;color:#333}
.person{font-weight:700;font-size:11px;color:#222;margin-top:5px}
.role{font-size:7.6px;color:var(--green-text);margin-top:3px}

.rule{left:0;top:962px;width:681px;height:1px;background:#ddd}
.partners{left:0;top:963px;width:681px;height:61px;display:flex;align-items:center;justify-content:center;gap:34px}
.partner{font-weight:700;font-size:17px;color:#1f1f1f;display:flex;align-items:center;gap:6px}
.partner i{width:10px;height:10px;border-radius:50%;background:#1f1f1f;display:inline-block}

.footer{left:0;top:1024px;width:681px;height:152px;background:var(--footer)}
.f-brand{left:23px;top:1062px;width:56px;font-weight:700;font-size:10px;color:#fff;line-height:1.15}
.f-about{left:84px;top:1055px;width:112px;font-size:7.5px;line-height:10px;color:#ddd}
.copy{left:23px;top:1117px;font-size:8px;color:#fff}
.f-title{font-family:"Russo One",sans-serif;font-weight:400;color:#ddd}
.f-links{font-size:8px;line-height:12.6px;color:#ccc}
.social{top:1078px;width:20px;height:20px;border-radius:50%;background:#777}
.f-news{left:510px;top:1108px;font-size:7.3px;line-height:9px;color:#fff}
.email{left:510px;top:1131px;width:97px;height:18px;background:#fff;font-size:7.5px;color:#333;padding:5px 8px}
.subscribe{left:607px;top:1131px;width:44px;height:18px;background:var(--green);color:#fff;font-size:7.5px;text-align:center;line-height:18px}
.bottombar{left:0;top:1176px;width:681px;height:24px;background:var(--bottom);text-align:center;font-size:8px;color:#eee;line-height:24px}
</style>
</head>
<body>
<div class="page">

  <header>
    <div class="abs topbar"></div>
    <div class="abs ip">Your IP address is <b>10.48.126.73</b></div>
    <div class="abs search">search ...</div>
    <div class="abs radio" style="left:598px"><i class="on"></i>local</div>
    <div class="abs radio" style="left:634px"><i></i>web</div>
    <div class="abs navbar"></div>
    <svg class="abs logo-tab" width="140" height="68" viewBox="0 0 140 68" aria-hidden="true">
      <polygon points="26,0 137,0 113,68 12,68" fill="#2e9a34"/>
    </svg>
    <div class="abs logo-name">Kelvar<br>Systems</div>
    <nav class="abs nav">
      <span>HOME</span><span>CLIENTS</span><span>SERVICES</span><span>SUPPORTS</span><span>TESTIMONIALS</span><span>CONTACT US</span><span>ABOUT US</span>
    </nav>
  </header>

  <section>
    <div class="abs hero" role="img" aria-label="Photo of a smiling technician plugging a cable into a computer tower while a colleague looks on"></div>
    <h1 class="abs hero-title">COMPANY WITH A SINGLE OBJECTIVE</h1>
    <p class="abs hero-sub">To excel in the support and service of all computer and IT needs.</p>
    <div class="abs code-input">Enter your 6-digit code</div>
    <div class="abs connect">CONNECT NOW</div>
  </section>

  <section>
    <div class="abs blush"></div>
    <div class="abs services"></div>
    <div class="abs more">+ more services</div>

    <div class="abs svc" style="left:43px;top:409px">
      <div class="svc-icon">
        <svg width="30" height="30" viewBox="0 0 30 30"><path d="M6 24 L20 10" stroke="#333" stroke-width="3.5" stroke-linecap="round"/><circle cx="21" cy="9" r="5" fill="none" stroke="#333" stroke-width="3"/><path d="M8 6 L24 22" stroke="#2e9a34" stroke-width="3.5" stroke-linecap="round"/></svg>
      </div>
      <h3>ON-SITE SERVICE</h3>
      <p>Ut wisi enim ad minim veniam, quis nostrud exerci tation ullamcorper suscipit lobortis nisl ut aliquip ex ea commodo consequat.</p>
    </div>
    <div class="abs svc" style="left:363px;top:409px">
      <div class="svc-icon">
        <svg width="32" height="30" viewBox="0 0 32 30"><rect x="3" y="4" width="26" height="17" rx="1" fill="none" stroke="#333" stroke-width="2.5"/><rect x="11" y="23" width="10" height="3" fill="#333"/><path d="M9 17 L22 7" stroke="#2e9a34" stroke-width="3" stroke-linecap="round"/></svg>
      </div>
      <h3>WEB DESIGN</h3>
      <p>Ut wisi enim ad minim veniam, quis nostrud exerci tation ullamcorper suscipit lobortis nisl ut aliquip ex ea commodo consequat.</p>
    </div>
    <div class="abs svc" style="left:43px;top:513px">
      <div class="svc-icon">
        <svg width="32" height="30" viewBox="0 0 32 30"><rect x="4" y="5" width="24" height="21" fill="none" stroke="#333" stroke-width="2.5"/><path d="M11 3 L19 5 L19 14 Q19 20 13 23 Q7 20 7 14 L7 5 Z" fill="#2e9a34" stroke="#333" stroke-width="1.5"/></svg>
      </div>
      <h3>SERVER &amp; SECURITY</h3>
      <p>Ut wisi enim ad minim veniam, quis nostrud exerci tation ullamcorper suscipit lobortis nisl ut aliquip ex ea commodo consequat.</p>
    </div>
    <div class="abs svc" style="left:363px;top:513px">
      <div class="svc-icon">
        <svg width="32" height="32" viewBox="0 0 32 32"><circle cx="16" cy="16" r="13" fill="#333"/><circle cx="16" cy="16" r="10" fill="none" stroke="#2e9a34" stroke-width="2"/><circle cx="16" cy="16" r="4" fill="#e8e8e8"/></svg>
      </div>
      <h3>HARDWARE &amp; SOFTWARE</h3>
      <p>Scripting, web apps, styling, mobile apps, desktop apps, databases and more!</p>
    </div>
  </section>

  <section>
    <h2 class="abs clients-title">Our Satisified Clients</h2>

    <div class="abs avatar" style="left:71px;top:737px" role="img" aria-label="Portrait of client Dorian Pellham"></div>
    <div class="abs avatar" style="left:304px;top:737px" role="img" aria-label="Portrait of client Ronald Ashby"></div>
    <div class="abs avatar" style="left:527px;top:737px" role="img" aria-label="Portrait of client Celia Marwood"></div>

    <div class="abs" style="left:23px;top:828px">
      <p class="quote">Vel illum dolore eu feugiat nulla facilisis at vero eros et accumsan et iusto dignissim qui blandit praesent lupt zril delenit augue duis dolore te feugait nulla facilisi.</p>
      <p class="person">Dorian Pellham</p>
      <p class="role">Accounting&nbsp; Officer</p>
    </div>
    <div class="abs" style="left:245px;top:828px">
      <p class="quote">Typi non habent claritatem insitam est us legentis in iis qui facit eorum claritatem. Investigationes demonstraverunt lectores legere me lius quod ii legunt saepius.</p>
      <p class="person">Ronald Ashby</p>
      <p class="role">Accounting&nbsp; Officer</p>
    </div>
    <div class="abs" style="left:474px;top:828px">
      <p class="quote">Claritas est etiam processus dynamicus sequitur mutationem consuetudium lectorum. Mirum est notare quam littera gothica, quam nunc pumus parum clam, anteposuerit litterarum formas.</p>
      <p class="person">Celia Marwood</p>
      <p class="role">President, CEO of Norvale Digital</p>
    </div>
  </section>

  <div class="abs rule"></div>
  <div class="abs partners">
    <span class="partner"><i></i>Corvex</span>
    <span class="partner">Brightlane</span>
    <span class="partner"><i></i>Norda</span>
    <span class="partner">Veltrix</span>
    <span class="partner">Stratova</span>
  </div>

  <footer>
    <div class="abs footer"></div>
    <div class="abs f-brand">Kelvar<br>Systems</div>
    <p class="abs f-about">Kelvar Systems is an Adelaide based company with a single objective - to excel in the support and service of all computer and IT needs.</p>
    <p class="abs copy">Copyright © 2013 Kelvar Systems Pty Ltd.</p>

    <h4 class="abs f-title" style="left:239px;top:1052px;font-size:12.5px">SERVICES</h4>
    <div class="abs f-links" style="left:240px;top:1076px">On-site Service<br>Remote Desktop Support<br>Medical IT Service<br>Pharmacy IT Service</div>
    <div class="abs f-links" style="left:356px;top:1076px">Website Design<br>Disaster Recovery<br>Hardware/ Software supply<br>Consumables</div>

    <h4 class="abs f-title" style="left:510px;top:1052px;font-size:12.8px">CONNECT WITH US</h4>
    <span class="abs social" style="left:509px"></span>
    <span class="abs social" style="left:535px"></span>
    <span class="abs social" style="left:560px"></span>
    <span class="abs social" style="left:585px"></span>
    <span class="abs social" style="left:610px"></span>
    <p class="abs f-news">subscribe to our monthly newsletter<br>and get the best deals and discounts</p>
    <div class="abs email">email address</div>
    <div class="abs subscribe">subscribe</div>

    <div class="abs bottombar">Home &nbsp;|&nbsp; Clients &nbsp;|&nbsp; Services &nbsp;|&nbsp; Supports &nbsp;|&nbsp; Testimonials &nbsp;|&nbsp; Contact Us &nbsp;|&nbsp; About us</div>
  </footer>

</div>
</body>
</html>
```